Awesome Office Furniture Dealer's Brochure!

Need a professional and informative brochure put together for our clients - may need separate designs for Government and Education clients. Should be based of our new website design and feel. Sections should include: Manufacturers we carry, services, and statements about our company - who we are & what we do. Brochure is 8.5 x 11 in tri-fold configuration. Template files attached.

Target Market(s)

Small to Medium businesses

Industry/Entity Type

Office Furniture

Requirements
Must have
• Look and feel of our website www.pembrills.com. Images can be taken from any of our vendors listed under /products, look to VEX primarily. We will get the final designer production ready images when needed.
Nice to have
• Incorporate the "love your workspace" from our website.

```html
<!DOCTYPE html>
<html lang="en">
<head>
<meta charset="utf-8">
<title>Pembrill's Office Furniture Brochure</title>
<link href="https://fonts.googleapis.com/css2?family=Open+Sans:wght@400;600;700;800&family=Dancing+Script:wght@600&display=swap" rel="stylesheet">
<style>
:root{
  --gold:#c4a23a;
  --orange:#ee8a1e;
  --green:#7cbf3f;
  --blue:#1f6fb8;
  --ink:#4a4a4a;
  --light:#ffffff;
}
*{margin:0;padding:0;box-sizing:border-box}
html,body{width:795px;height:1200px;overflow:hidden;background:var(--gold)}
body{font-family:"Open Sans",Arial,sans-serif;color:var(--ink);position:relative}
.panel{position:absolute;left:22px;width:751px;background:var(--light);overflow:hidden}
.panel-front{top:24px;height:566px}
.panel-inside{top:612px;height:566px}
.photo{position:absolute}
.wave{position:absolute;left:0;width:100%}

/* front cover */
.front-photo{left:0;top:0;width:751px;height:400px;
  background:linear-gradient(100deg,#5f86b4 0%,#c9d3da 14%,#eef1f3 32%,#dfe5e9 55%,#c7d0d6 72%,#e9a86a 88%,#f07e2a 100%)}
.front-photo::after{content:"";position:absolute;inset:0;
  background:linear-gradient(180deg,rgba(255,255,255,.55) 0%,rgba(255,255,255,0) 35%,rgba(90,110,130,.18) 70%,rgba(210,190,160,.35) 100%)}
.front-chair{left:36px;top:412px;width:48px;height:90px;background:linear-gradient(180deg,#f09a3c 0%,#f3b57a 45%,#e4e4e4 100%)}
.tagline{position:absolute;left:18px;top:512px;font-family:"Dancing Script",cursive;font-size:26px;color:#2e2e2e}
.contact{position:absolute;left:290px;top:402px;width:180px;text-align:center;font-size:12px;line-height:18px}
.contact .phone{color:var(--blue);font-weight:700}
.contact .web{color:var(--green);font-weight:700;margin-top:4px;letter-spacing:.5px}
.brand{position:absolute;left:518px;top:436px;display:flex;align-items:center;gap:10px}
.brand-mark{width:30px;height:30px;background:var(--ink)}
.brand-name{font-size:32px;font-weight:800;color:var(--orange);line-height:1}
.brand-sub{font-size:10px;font-weight:700;color:var(--orange);letter-spacing:1.5px;margin-top:5px}

/* inside */
.why{position:absolute;left:14px;top:14px;width:222px;font-size:7.6px;line-height:10.6px}
.why h2{font-size:9.5px;font-weight:700;color:var(--orange);text-align:center;letter-spacing:.3px;margin-bottom:6px}
.why .promise{background:var(--orange);color:#fff;font-weight:700;font-size:10px;line-height:13px;text-align:center;padding:5px 8px;margin-bottom:8px}
.why p{margin-bottom:7px}
.why .lead{color:var(--orange);font-weight:700}
.inside-photo{left:246px;top:0;width:250px;height:350px;
  background:linear-gradient(90deg,#b9c3c9 0%,#e9eef1 25%,#f7f9fa 50%,#dfe5e8 75%,#aeb9c0 100%)}
.inside-photo::after{content:"";position:absolute;inset:0;
  background:linear-gradient(180deg,rgba(255,255,255,.6) 0%,rgba(255,255,255,0) 40%,rgba(120,135,145,.3) 100%)}
.values{position:absolute;left:508px;top:14px;width:232px;font-size:7.6px;line-height:10.2px;text-align:center}
.values h2{font-size:13px;font-weight:700;color:var(--green);margin-bottom:8px}
.values h3{font-size:8.5px;color:var(--orange);font-weight:700;margin-bottom:1px}
.values p{margin-bottom:8px}
.inside-chair{left:606px;top:262px;width:56px;height:92px;background:linear-gradient(180deg,#2f2f2f 0%,#555 60%,#8a8a8a 100%)}
.floor-photo{left:0;top:340px;width:751px;height:226px;
  background:linear-gradient(95deg,#8d9aa2 0%,#dde3e6 18%,#f3f5f6 40%,#c9d1d5 60%,#eef1f2 80%,#9aa6ad 100%)}
.floor-photo::after{content:"";position:absolute;inset:0;
  background:linear-gradient(180deg,rgba(255,255,255,.5) 0%,rgba(60,70,80,.25) 55%,rgba(230,232,232,.6) 100%)}
</style>
</head>
<body>

<section class="panel panel-front">
  <div class="photo front-photo" role="img" aria-label="Open-plan office with white cubicle workstations, blue task chairs and an orange feature wall"></div>
  <svg class="wave" style="top:320px" width="751" height="100" viewBox="0 0 751 100" aria-hidden="true">
    <path d="M0 72 C230 58 460 40 751 16 L751 100 L0 100 Z" fill="var(--light)"/>
    <path d="M0 62 C230 48 460 28 751 2 L751 12 C460 38 230 58 0 72 Z" fill="var(--blue)"/>
    <path d="M0 76 C230 62 460 44 751 22 L751 32 C460 54 230 72 0 86 Z" fill="var(--green)"/>
  </svg>
  <div class="photo front-chair" role="img" aria-label="Orange and white designer chair"></div>
  <p class="tagline">Love your workspace!</p>
  <div class="contact">
    <p>Call us @</p>
    <p>Seattle <span class="phone">206.555.0142</span></p>
    <p>or</p>
    <p>Bellevue <span class="phone">425.555.0188</span></p>
    <p class="web">WWW.PEMBRILLS.COM</p>
  </div>
  <div class="brand">
    <span class="brand-mark"></span>
    <div>
      <p class="brand-name">PEMBRILL'S</p>
      <p class="brand-sub">OFFICE FURNITURE</p>
    </div>
  </div>
</section>

<section class="panel panel-inside">
  <div class="why">
    <h2>WHY PEMBRILL'S OFFICE FURNITURE?</h2>
    <div class="promise">Because we make buying office furniture easy.</div>
    <p><span class="lead">First, we know what we are doing.</span> With over 30 years of experience in commercial furniture, you can count on our knowledgeable staff to help you through the entire buying process from design to product choice to final installation.</p>
    <p><span class="lead">Second, we listen to our clients.</span> If you have a budget, we stick to it. If you don't like a product, we don't need to sell it to you. We take time to understand your goals before we ever suggest a single piece.</p>
    <p><span class="lead">Third, we stay with what we believe in.</span> Every product we carry has been tested by our team, from VEX seating to custom casework, so you get furniture that lasts.</p>
    <p><span class="lead">Last, we believe we offer the best value.</span> Competitive pricing, careful planning and dependable service are included on every project, large or small.</p>
  </div>

  <div class="photo inside-photo" role="img" aria-label="Bright modern office interior with ceiling lights and workstations"></div>

  <div class="values">
    <h2>OUR CORE VALUES</h2>
    <h3>Dedication to Customer Service Excellence</h3>
    <p>We will meet and exceed customer needs and expectations. We will provide a relaxed buying experience with professional guidance and support.</p>
    <h3>Honesty &amp; Integrity</h3>
    <p>We will conduct all of our business with uncompromising honesty, integrity and trust to earn the highest ethical standard.</p>
    <h3>People Growth &amp; Development</h3>
    <p>We will demonstrate care and respect for all members of the team, their families, our neighbors, customers and suppliers.</p>
    <h3>Product Quality</h3>
    <p>We will provide solutions to our customers which exemplify our commitment to value, products that are high quality, reasonably priced and well designed.</p>
  </div>

  <div class="photo inside-chair" role="img" aria-label="Black mesh ergonomic office chair"></div>

  <div class="photo floor-photo" role="img" aria-label="Wide view of an open office floor with white desks and black chairs"></div>
  <svg class="wave" style="top:300px" width="751" height="90" viewBox="0 0 751 90" aria-hidden="true">
    <path d="M0 0 L751 0 L751 58 C500 60 250 66 0 76 Z" fill="var(--light)"/>
    <path d="M0 62 C250 52 500 46 751 44 L751 54 C500 56 250 62 0 72 Z" fill="var(--green)"/>
    <path d="M0 76 C250 66 500 60 751 58 L751 64 C500 66 250 72 0 82 Z" fill="var(--blue)"/>
  </svg>
</section>

</body>
</html>
```